Cyber Security firm requires new branding and website design

We are open to advice on project budget so feel free to message me regarding this. We understand there are people from all over the world looking at this so initially we may be looking at just a landing page to just give us an idea of the design and that can be enough to win this contest. From there we can agree a reward / payment for the whole site.
We're looking for a Designer with UI/UX and some branding skills. We really need someone to give us a direction and then create a mock-up in Photoshop. We have a great logo and so far our website has done the job but is very basic www.vandrelock.com . We can reuse most the content (and this can be used by the Designer) but we need a complete redesign. Keep it clear, simple, classy and uncluttered and we certainly need new color scheme.
I have attached our logo's and a copy of our business cards (the black logo is actually silver foil) to give you an idea of the sort of branding we like.
We are based in Los Angeles and our clients range from the Entertainment business and start-ups to Law and Financial firms so we need a site design that appeals to all of these sectors.
Once we have the design we can give it to our developer to turn into a working site.
Updates
I wasn't sure how this worked as its the first time I have used the site.
Happy to take feedback on what would be most attractive to you guys to get you to want to design for us.
Cheers
Tomas
The styles we like personally tend to have blocks of content and some funky HTML 5 stuff (If you can design it we can code it). Here are some examples:
http://www.plumo.co
http://quillbendpilates.com/
http://harborweave.com/
We are a fun company and have a good sense of humor. Our client generally do too but they are also dealing with serious issues so if you can get something that's fun but puts across that we are serious about what we do that would be great. Oh and we love this one so if you can take some influence from this but keep it professional we would love to see it:
http://mildcometworks.com/
I also like the old typewriter style lettering i have seen used on contact forms. However this has to be a cohesive design so we want you to add what looks right not just everything we like (unless you can do that well).
We understand that you show a static site so this is hard to demonstrate but we particularly like the videos people are embedding nowadays and would love to avoid stock photos where we can:
https://www.coinvesta.com/home
Hopefully this gives you all more food for thought.
Industry/Entity Type
Business
Colors
Designer to choose colors to be used in the design.
Look and feel
Each slider illustrates characteristics of the customer's brand and the style your logo design should communicate.

```html
<!DOCTYPE html>
<html lang="en">
<head>
<meta charset="utf-8">
<title>Vandrelock Security</title>
<link rel="stylesheet" href="https://fonts.googleapis.com/css2?family=Open+Sans:wght@300;400;600;700&family=Raleway:wght@300;400;600;700&display=swap">
<style>
:root{
  --ink:#2b2b2b;
  --muted:#7a7a7a;
  --line:#dcdcdc;
  --band:#efefef;
  --dark:#2e2e2e;
  --darker:#232323;
  --accent:#4a4a4a;
  --white:#ffffff;
}
*{box-sizing:border-box;margin:0;padding:0}
html,body{width:1200px;height:2360px;overflow:hidden}
body{font-family:"Open Sans",Arial,sans-serif;color:var(--ink);background:var(--white);font-size:13px}
.wrap{width:1080px;margin:0 auto;position:relative}

.site-header{height:140px;border-bottom:1px solid var(--line)}
.site-header .wrap{height:140px;display:flex;align-items:center;justify-content:space-between}
.brand{display:flex;align-items:center;gap:12px;font-family:"Raleway",sans-serif;font-weight:600;font-size:22px;letter-spacing:2px;color:var(--ink)}
.brand-mark{width:34px;height:34px;background:var(--accent)}
.header-right{display:flex;flex-direction:column;align-items:flex-end;gap:22px}
.header-contact{font-size:12px;color:var(--muted);text-align:right;line-height:1.5}
.main-nav{display:flex;gap:28px;font-family:"Raleway",sans-serif;font-size:12px;font-weight:600;letter-spacing:1px;color:var(--muted)}
.main-nav .active{color:var(--ink);border-bottom:2px solid var(--ink);padding-bottom:4px}

.hero{height:460px;position:relative;background:linear-gradient(90deg,#3a3a3a 0%,#5b5b5b 45%,#2c2c2c 100%)}
.hero-media{position:absolute;inset:0;background:radial-gradient(ellipse at 58% 45%,#6e6e6e 0%,#454545 40%,#262626 85%)}
.hero-copy{position:absolute;left:60px;top:175px;color:var(--white)}
.hero-copy h1{font-family:"Raleway",sans-serif;font-weight:700;font-size:30px;letter-spacing:1px;line-height:1.25}
.btn{display:inline-block;font-family:"Raleway",sans-serif;font-size:11px;font-weight:700;letter-spacing:1px;padding:9px 16px;text-transform:uppercase}
.btn-light{background:var(--white);color:var(--ink);margin-top:16px}
.btn-outline{border:1px solid var(--line);color:var(--ink);background:var(--white)}
.btn-dark{background:var(--accent);color:var(--white)}
.hero-arrow{position:absolute;top:210px}
.hero-arrow.left{left:18px}
.hero-arrow.right{right:18px}

.welcome{height:300px}
.welcome .wrap{display:flex;gap:40px;padding-top:50px}
.welcome-media{width:245px;height:175px;background:linear-gradient(135deg,#e8eef4,#b9c8d8);flex:none}
.welcome-copy h2{font-family:"Raleway",sans-serif;font-size:22px;font-weight:700;letter-spacing:1px;margin-bottom:14px}
.welcome-copy p{color:var(--muted);line-height:1.7;max-width:740px;margin-bottom:18px}

.reasons{background:var(--band);height:450px;padding-top:46px}
.section-title{text-align:center;font-family:"Raleway",sans-serif;font-weight:700;font-size:22px;letter-spacing:1px}
.rule{width:520px;height:1px;background:#cfcfcf;margin:22px auto 34px}
.reason-grid{display:grid;grid-template-columns:repeat(3,1fr);gap:44px 60px;padding:0 40px}
.reason h3{display:flex;align-items:center;gap:10px;font-family:"Raleway",sans-serif;font-size:20px;font-weight:600;margin-bottom:10px}
.reason p{color:var(--muted);font-size:11.5px;line-height:1.6}

.services{padding-top:36px;height:340px}
.services-title{text-align:center;font-family:"Raleway",sans-serif;font-weight:300;font-size:44px;letter-spacing:1px}
.service-grid{display:grid;grid-template-columns:repeat(4,1fr);gap:24px;margin-top:20px}
.service-media{height:135px}
.service h4{font-family:"Raleway",sans-serif;font-size:16px;font-weight:700;margin-top:12px}
.service span{font-size:11px;color:var(--muted)}

.news{margin-top:10px}
.news-card{display:flex;align-items:center;border:1px solid var(--line);height:90px;width:960px;margin:0 auto;position:relative}
.news-date{width:68px;height:100%;background:var(--accent);color:var(--white);font-family:"Raleway",sans-serif;font-weight:700;display:flex;flex-direction:column;align-items:center;justify-content:center;font-size:13px}
.news-date b{font-size:26px}
.news-body{padding:0 20px}
.news-body h5{font-size:15px;font-weight:600;margin-bottom:6px}
.news-body p{font-size:11px;color:var(--muted);width:780px;line-height:1.5}
.news-card svg{position:absolute;right:16px;top:34px}

.job{text-align:center;padding-top:40px;height:180px}
.job h5{font-family:"Raleway",sans-serif;font-size:21px;font-weight:600;color:var(--ink)}
.job h5 small{font-size:11px;color:var(--muted);font-weight:400}
.job-actions{margin-top:18px;display:flex;justify-content:center;gap:10px}

.contact-bar{background:var(--darker);height:48px;color:#ddd;font-size:14px}
.contact-bar .wrap{display:flex;justify-content:center;align-items:center;gap:56px;height:48px}
.contact-bar span{display:flex;align-items:center;gap:8px}

.site-footer{background:var(--dark);height:278px;color:#bdbdbd;padding-top:38px}
.footer-grid{display:grid;grid-template-columns:1.3fr 1fr 1fr 1fr 1fr;gap:30px}
.footer-col h6{font-family:"Raleway",sans-serif;font-size:12px;font-weight:700;letter-spacing:1px;color:var(--white);margin-bottom:12px}
.footer-col ul{list-style:none;font-size:11.5px;line-height:1.9}
.footer-col .two{display:grid;grid-template-columns:1fr 1fr}
.news-input{width:160px;height:26px;background:var(--white);margin-bottom:10px}
.social{display:flex;gap:8px}
.social i{width:22px;height:22px;background:#777;display:block}
.legal{background:var(--darker);height:54px;color:#9a9a9a;font-size:11px}
.legal .wrap{display:flex;justify-content:space-between;align-items:center;height:54px}
.legal .links{display:flex;gap:14px}
.legal .copy{margin-top:4px}
</style>
</head>
<body>

<header class="site-header">
  <div class="wrap">
    <div class="brand"><span class="brand-mark"></span>VANDRELOCK SECURITY</div>
    <div class="header-right">
      <div class="header-contact">E-mail<br>support@vandrelock.com</div>
      <nav class="main-nav">
        <span class="active">HOME</span><span>PENETRATION TESTING</span><span>STAFFING</span><span>HOT JOBS</span><span>NEWS</span><span>ABOUT</span><span>CONTACT</span>
      </nav>
    </div>
  </div>
</header>

<section class="hero">
  <div class="hero-media" role="img" aria-label="Hooded figure at a laptop in front of a chalkboard of security words"></div>
  <div class="hero-copy">
    <h1>ALIQUAM ERAT<br>VOLUTPAT</h1>
    <span class="btn btn-light">Contact us</span>
  </div>
  <svg class="hero-arrow left" width="20" height="36" viewBox="0 0 20 36"><path d="M16 2 2 18l14 16" fill="none" stroke="#fff" stroke-width="3"/></svg>
  <svg class="hero-arrow right" width="20" height="36" viewBox="0 0 20 36"><path d="M4 2l14 16L4 34" fill="none" stroke="#fff" stroke-width="3"/></svg>
</section>

<section class="welcome">
  <div class="wrap">
    <div class="welcome-media" role="img" aria-label="Blue digital padlock on a light background"></div>
    <div class="welcome-copy">
      <h2>WELCOME TO VANDRELOCK SECURITY</h2>
      <p>Vandrelock Security is a specialist penetration testing company assisting organisations of every size in protecting against an array of system threats. Founded by a veteran team of dedicated ethical hackers with over 25 years of IT security experience, Vandrelock Security makes sure your company's IT network is thoroughly tested and safe guarded against malicious attacks.</p>
      <span class="btn btn-outline">Read more</span>
    </div>
  </div>
</section>

<section class="reasons">
  <h2 class="section-title">6 REASONS WHY YOUR COMPANY NEEDS AN IT SECURITY AUDIT</h2>
  <div class="rule"></div>
  <div class="wrap">
    <div class="reason-grid">
      <div class="reason"><h3><svg width="18" height="18" viewBox="0 0 18 18"><circle cx="9" cy="9" r="9" fill="#4a4a4a"/><path d="M5 9l3 3 5-6" fill="none" stroke="#fff" stroke-width="2"/></svg>Focus</h3><p>Teams have penetration tests to prove gaps before attackers do, keeping systems focused on the real threats that hurt companies.</p></div>
      <div class="reason"><h3><svg width="18" height="18" viewBox="0 0 18 18"><circle cx="9" cy="9" r="9" fill="#4a4a4a"/><path d="M5 9l3 3 5-6" fill="none" stroke="#fff" stroke-width="2"/></svg>Zero Day Exploits</h3><p>New flaws appear in systems daily and software frequently has unknown weak spots that only careful testing will reveal.</p></div>
      <div class="reason"><h3><svg width="18" height="18" viewBox="0 0 18 18"><circle cx="9" cy="9" r="9" fill="#4a4a4a"/><path d="M5 9l3 3 5-6" fill="none" stroke="#fff" stroke-width="2"/></svg>Undetected Breaches</h3><p>Many companies do not even realise they have been compromised until long after data has left the building.</p></div>
      <div class="reason"><h3><svg width="18" height="18" viewBox="0 0 18 18"><circle cx="9" cy="9" r="9" fill="#4a4a4a"/><path d="M5 9l3 3 5-6" fill="none" stroke="#fff" stroke-width="2"/></svg>Mobile Data Exposure</h3><p>Mobile devices carry sensitive company data and are often the easiest point of entry for a determined attacker.</p></div>
      <div class="reason"><h3><svg width="18" height="18" viewBox="0 0 18 18"><circle cx="9" cy="9" r="9" fill="#4a4a4a"/><path d="M5 9l3 3 5-6" fill="none" stroke="#fff" stroke-width="2"/></svg>Global Hacking</h3><p>Organised hacker groups work around the clock worldwide, probing networks for any opening they can use.</p></div>
      <div class="reason"><h3><svg width="18" height="18" viewBox="0 0 18 18"><circle cx="9" cy="9" r="9" fill="#4a4a4a"/><path d="M5 9l3 3 5-6" fill="none" stroke="#fff" stroke-width="2"/></svg>Cloud Security</h3><p>Companies store more in the cloud than ever, yet few have reviewed who can actually reach that information.</p></div>
    </div>
  </div>
</section>

<section class="services">
  <h2 class="services-title">OUR SERVICES</h2>
  <div class="wrap">
    <div class="service-grid">
      <div class="service"><div class="service-media" role="img" aria-label="Team reviewing screens in an office" style="background:linear-gradient(135deg,#c9d4de,#7c8c9c)"></div><h4>Emergency Response</h4><span>Contract Staffing</span></div>
      <div class="service"><div class="service-media" role="img" aria-label="Colleagues meeting around a desk" style="background:linear-gradient(135deg,#dfe6ec,#93a3b1)"></div><h4>Tactical</h4><span>Contingency permanent staffing</span></div>
      <div class="service"><div class="service-media" role="img" aria-label="Consultant working at a laptop" style="background:linear-gradient(135deg,#eef1f4,#a9b4be)"></div><h4>Covert</h4><span>Executive Search</span></div>
      <div class="service"><div class="service-media" role="img" aria-label="Silhouettes of business people against a bright window" style="background:linear-gradient(135deg,#f2f2f2,#8f8f8f)"></div><h4>Strategic</h4><span>Project outsourcing</span></div>
    </div>
  </div>
</section>

<section class="news">
  <div class="news-card">
    <div class="news-date"><b>22</b>JAN</div>
    <div class="news-body">
      <h5>Vandrelock Security founder to present at Media Safeguard Forum</h5>
      <p>In the last year, and specifically the last quarter, there is a significant increase in threats against the studios, highlighting the need for attention to security in post houses, VFX studios and content delivery networks.</p>
    </div>
    <svg width="12" height="22" viewBox="0 0 12 22"><path d="M2 2l8 9-8 9" fill="none" stroke="#999" stroke-width="2"/></svg>
  </div>
</section>

<section class="job">
  <h5>Trainee Recruitment Consultant - Vandrelock Security - Culver City, CA <small>(Jan 21, Full Time)</small></h5>
  <div class="job-actions"><span class="btn btn-dark">Apply now</span><span class="btn btn-dark">View all jobs</span></div>
</section>

<div class="contact-bar">
  <div class="wrap">
    <span><svg width="14" height="14" viewBox="0 0 14 14"><path d="M3 1l2 3-1.5 1.5a8 8 0 0 0 5 5L10 9l3 2-1 2.5C6 13 1 8 .5 2z" fill="#ddd"/></svg>Contact us today! +1 (424) 555-0182</span>
    <span><svg width="12" height="16" viewBox="0 0 12 16"><path d="M6 0a6 6 0 0 0-6 6c0 4 6 10 6 10s6-6 6-10a6 6 0 0 0-6-6z" fill="#ddd"/><circle cx="6" cy="6" r="2" fill="#232323"/></svg>Find our Location</span>
    <span><svg width="16" height="12" viewBox="0 0 16 12"><rect width="16" height="12" fill="#ddd"/><path d="M0 0l8 6 8-6" fill="none" stroke="#232323" stroke-width="1.5"/></svg>support@vandrelock.com</span>
  </div>
</div>

<footer class="site-footer">
  <div class="wrap">
    <div class="footer-grid">
      <div class="footer-col"><h6>NAVIGATION</h6><div class="two"><ul><li>Home</li><li>Penetration Testing</li><li>Staffing</li><li>Hot Jobs</li></ul><ul><li>News</li><li>About</li><li>Contact</li></ul></div></div>
      <div class="footer-col"><h6>STAFFING</h6><ul><li>Staffing Solutions</li><li>Healthcare Hiring</li><li>Legal Utilities</li><li>Start-up Advice</li></ul></div>
      <div class="footer-col"><h6>ABOUT</h6><ul><li>Our Mission</li><li>Corporate Social Responsibility</li></ul></div>
      <div class="footer-col"><h6>CONTACT US</h6><ul><li>Customer Support</li><li>Request a Survey</li><li>Submit a Resume</li></ul></div>
      <div class="footer-col"><h6>NEWSLETTER</h6><div class="news-input"></div><div class="social"><i></i><i></i></div></div>
    </div>
  </div>
</footer>

<div class="legal">
  <div class="wrap">
    <div><div class="links"><span>Home</span><span>Contact Us</span><span>About Us</span><span>Sitemap</span><span>Privacy Policy</span></div><div class="copy">Copyright © 2015 · Vandrelock Security LLC · All rights reserved</div></div>
    <svg width="56" height="22" viewBox="0 0 56 22"><circle cx="11" cy="11" r="10" fill="none" stroke="#9a9a9a"/><circle cx="45" cy="11" r="10" fill="none" stroke="#9a9a9a"/></svg>
  </div>
</div>

</body>
</html>
```